Business Card Re-design

We are looking for a fresh bold look for general office business cards. We are a staffing agency that staffs industrial, coal mining, and clerical jobs.
Tag Line: We match the RIGHT talent with the RIGHT roles.
Marrowby Office: 437 W. Hollowmere Ave, Marrowby, IN - 47298
p. 402.555.0183 f. 402.555.0196
Quillfield Office: 926 S. Larkfen Way, Quillfield, IN - 47231
p. 402.555.0127 f. 402.555.0196
Absentee/Emergency 24hr Hotline 402.555.0164 opt.1
www.tallowcrestworkforce.example

```html
<!DOCTYPE html>
<html lang="en">
<head>
<meta charset="utf-8">
<title>Tallowcrest Workforce – Business Card</title>
<link href="https://fonts.googleapis.com/css2?family=Arimo:wght@700&family=Ubuntu:wght@500&display=swap" rel="stylesheet">
<style>
  :root {
    --card-red: #ff0000;
    --white: #ffffff;
    --ink: #111111;
    --bg-top: #959382;
    --bg-mid: #d2d0c8;
    --bg-bottom: #ffffff;
  }
  * { margin: 0; padding: 0; box-sizing: border-box; }
  html, body { width: 1200px; height: 1200px; overflow: hidden; }
  body {
    position: relative;
    background: linear-gradient(to bottom, var(--bg-top) 0%, var(--bg-mid) 50%, var(--bg-bottom) 100%);
  }
  .card {
    position: absolute;
    left: 192px;
    width: 851px;
    height: 519px;
    background: var(--card-red);
    overflow: hidden;
  }
  .card--front { top: 34px; }
  .card--back { top: 618px; }
  .card svg.decor { position: absolute; left: 0; top: 0; }

  .brand-name {
    position: absolute;
    font-family: "Ubuntu", sans-serif;
    font-weight: 500;
    color: var(--card-red);
    text-align: center;
    line-height: 1;
    white-space: nowrap;
  }
  .brand-name--large { left: 132px; width: 596px; top: 240px; font-size: 46px; }
  .brand-name--small { left: 639px; width: 162px; top: 428px; font-size: 14px; }

  .tagline {
    position: absolute;
    left: 0; width: 100%;
    top: 77px;
    text-align: center;
    font-family: "Ubuntu", sans-serif;
    font-weight: 500;
    font-size: 27px;
    color: var(--white);
  }
  .contact {
    position: absolute;
    left: 154px;
    font-family: "Arimo", sans-serif;
    font-weight: 700;
    font-size: 19px;
    line-height: 24px;
    color: var(--white);
    letter-spacing: -0.2px;
    white-space: nowrap;
  }
  .contact--main { top: 186px; }
  .contact--branch { top: 250px; }
  .contact--hotline { top: 317px; }
  .contact--web { top: 385px; }
</style>
</head>
<body>

<section class="card card--front">
  <svg class="decor" width="851" height="519" viewBox="0 0 851 519">
    <ellipse cx="430" cy="263" rx="308" ry="184" fill="none" stroke="var(--white)" stroke-width="12" transform="rotate(-3 430 263)"/>
    <ellipse cx="430" cy="263" rx="298" ry="168" fill="var(--white)" stroke="#222" stroke-width="1"/>
  </svg>
  <div class="brand-name brand-name--large">Tallowcrest Workforce</div>
</section>

<section class="card card--back">
  <svg class="decor" width="851" height="519" viewBox="0 0 851 519">
    <path d="M24 67 Q425 45 826 67 Q425 52 24 67 Z" fill="var(--white)" stroke="var(--white)" stroke-width="1.5"/>
    <path d="M24 117 Q425 140 826 117 Q425 132 24 117 Z" fill="var(--white)" stroke="var(--white)" stroke-width="1.5"/>

    <g transform="translate(104 210)">
      <polygon points="-20,0 -10,-18 10,-18 20,0 10,18 -10,18" fill="var(--white)"/>
      <path d="M-10 -1 L0 -10 L10 -1 M-6 -3 V8 H6 V-3" fill="none" stroke="var(--ink)" stroke-width="2.4" stroke-linejoin="round"/>
    </g>
    <g transform="translate(104 330)">
      <polygon points="-20,0 -10,-18 10,-18 20,0 10,18 -10,18" fill="var(--white)"/>
      <path d="M-6 -9 Q-10 -2 -4 5 Q2 11 8 8 L5 3 L1 5 Q-3 1 -2 -3 L0 -5 Z" fill="var(--ink)"/>
    </g>
    <g transform="translate(104 398)">
      <polygon points="-20,0 -10,-18 10,-18 20,0 10,18 -10,18" fill="var(--white)"/>
      <circle r="10" fill="var(--ink)"/>
      <g stroke="var(--white)" stroke-width="1.2" fill="none">
        <ellipse rx="4.5" ry="10"/>
        <line x1="-10" y1="0" x2="10" y2="0"/>
        <line x1="-9" y1="-5" x2="9" y2="-5"/>
        <line x1="-9" y1="5" x2="9" y2="5"/>
        <line x1="0" y1="-10" x2="0" y2="10"/>
      </g>
    </g>

    <ellipse cx="720" cy="435" rx="86" ry="50" fill="none" stroke="var(--white)" stroke-width="4" transform="rotate(-3 720 435)"/>
    <ellipse cx="720" cy="435" rx="81" ry="46" fill="var(--white)" stroke="#222" stroke-width="0.6"/>
  </svg>

  <p class="tagline">We match the RIGHT talent with the RIGHT roles</p>

  <p class="contact contact--main">Marrowby Office: 437 W. Hollowmere Ave, Marrowby, IN - 47298<br>p. 402.555.0183 f. 402.555.0196</p>
  <p class="contact contact--branch">Quillfield Office: 926 S. Larkfen Way, Quillfield, IN - 47231<br>p. 402.555.0127 f. 402.555.0196</p>
  <p class="contact contact--hotline">Absentee/Emergency 24hr Hotline 402.555.0164</p>
  <p class="contact contact--web">www.tallowcrestworkforce.example</p>

  <div class="brand-name brand-name--small">Tallowcrest Workforce</div>
</section>

</body>
</html>
```